Business Card - high end, modern health care

Hey designers!

We need a double sided business card for the boutique, cutting edge physical therapy rehabilitation centre in Sydney's Northern Beaches.

With the most qualified physios in the area The Harbourline Motion Clinic does what other physiotherapy practices do not, we take our time with our patients giving them longer appointments, better physios and therefor faster results!

We guarantee that the service people receive at THMC will be unparalleled.

Hence we need a business card to reflect our modern, boutique, high end service. The final design needs to reflect that we are in a class of our own yet with the feel of beachside retreat.

Below I have attached our logo in both blue on white and white on blue. The exact colour is;
and the font that we have used in our logo is Tex Gyre Aventador.

I like the idea of the blue as the main colour as it is more eye catching and our signage onto the main road will be in this blue and in the interest of consistency across marketing the blue needs to be a part of the design. However I would appreciate a few designs onto a wooden background as this is a visual theme within the fitout of the practice.

The design needs to be of standard size (91x55mm).

Target Market(s)

We target people who have an end outcome in mind and those who have had poor experiences with other providers and ensure that everyone gets the care that they deserve with a premium service that is tailored to the individuals circumstances. As a premium service, the target market is highly educated, business and tech savvy with the additional target market of elderly people who have self funded their retirement and see value in paying for the best ongoing rehabilitation to maintain independence.

Industry/Entity Type

Physical Therapy

Contact Information for Business Card

Name, designation( Titled Musculoskeletal Physiotherapist... there will also be those in the company that have multiple designations ie 5 or 6 words long), phone number, email, facebook, instagram, address

Font styles to use
Sans Serif

Colors

Designer to choose colors to be used in the design.

Requirements
Must have
• Front - The logo as large as possible, blue or wooden theme, and all of the important details.
• Back - A blank space/lines on which to write appointment times (no "Appointment, date, time" etc.)
Nice to have
• facebook url
• logos for facebook and instagram
• Mini logos for the phone and email?

```html
<!DOCTYPE html>
<html lang="en">
<head>
<meta charset="utf-8">
<title>The Harbourline Motion Clinic — Business Card</title>
<link href="https://fonts.googleapis.com/css2?family=Montserrat:wght@600&family=Lato:wght@400;700&display=swap" rel="stylesheet">
<style>
  :root {
    --brand-blue: #0b57a8;
    --card-white: #f1f1f1;
    --ink: #2b2b2b;
    --rule-dark: #3a3a3a;
    --mark-faint: #dcdcdc;
    --white: #ffffff;
    --rule-light: rgba(255,255,255,0.45);
    --backdrop: #e6e6e6;
  }
  * { box-sizing: border-box; margin: 0; padding: 0; }
  html, body { width: 1200px; height: 782px; overflow: hidden; }
  body {
    background: var(--backdrop);
    font-family: "Lato", Arial, sans-serif;
    position: relative;
  }
  .card {
    position: absolute;
    top: 228px;
    width: 540px;
    height: 326px;
    box-shadow: 0 6px 18px rgba(0,0,0,0.18);
    overflow: hidden;
  }
  /* Front */
  .card-front { left: 40px; background: var(--brand-blue); color: var(--white); }
  .brand {
    position: absolute; left: 178px; top: 48px;
    display: flex; align-items: center; gap: 12px;
  }
  .brand-dot { width: 50px; height: 50px; border-radius: 50%; background: var(--white); flex: none; }
  .brand-name {
    font-family: "Montserrat", Arial, sans-serif; font-weight: 600;
    line-height: 1; color: var(--white);
  }
  .brand-name .line-1 { display: block; font-size: 27px; letter-spacing: 0.5px; }
  .brand-name .line-2 { display: block; font-size: 15px; letter-spacing: 6.2px; margin-top: 6px; }
  .person { position: absolute; left: 34px; top: 128px; }
  .person-name { font-weight: 700; font-size: 16px; letter-spacing: 0.6px; }
  .person-role { font-size: 12.5px; margin-top: 2px; }
  .social { position: absolute; left: 34px; top: 178px; font-size: 13px; line-height: 20px; }
  .social li { list-style: none; display: flex; align-items: center; gap: 7px; }
  .social-dot { width: 13px; height: 13px; border-radius: 50%; background: var(--white); }
  .divider { position: absolute; left: 34px; right: 34px; height: 1px; background: var(--rule-light); }
  .divider-top { top: 170px; width: 180px; }
  .divider-bottom { top: 236px; }
  .contact { position: absolute; right: 34px; top: 252px; font-size: 14.5px; line-height: 24px; text-align: right; }
  .contact li { list-style: none; display: flex; justify-content: flex-end; align-items: center; gap: 7px; }
  .contact svg { width: 15px; height: 15px; }
  /* Back */
  .card-back { left: 620px; background: var(--card-white); color: var(--ink); }
  .mark-faint {
    position: absolute; left: 222px; top: 44px;
    width: 240px; height: 240px; border-radius: 50%; background: var(--mark-faint);
  }
  .appointment-field { position: absolute; left: 82px; width: 390px; }
  .appointment-field .label { font-size: 14px; letter-spacing: 0.5px; text-transform: uppercase; }
  .appointment-field .rule { height: 1px; background: var(--rule-dark); margin-top: 2px; }
  .field-date { top: 96px; }
  .field-time { top: 156px; }
  .field-extra { top: 216px; }
</style>
</head>
<body>

<section class="card card-front" aria-label="Business card front">
  <div class="brand">
    <span class="brand-dot"></span>
    <span class="brand-name">
      <span class="line-1">THE HARBOURLINE</span>
      <span class="line-2">MOTION CLINIC</span>
    </span>
  </div>

  <div class="person">
    <p class="person-name">MARCUS HALE</p>
    <p class="person-role">Managing Director</p>
  </div>
  <div class="divider divider-top"></div>

  <ul class="social">
    <li><span class="social-dot"></span>/harbourlinemotionclinic</li>
    <li><span class="social-dot"></span>@harbourlinemotionclinic</li>
  </ul>

  <div class="divider divider-bottom"></div>

  <ul class="contact">
    <li>444 555 7012
      <svg viewBox="0 0 16 16" aria-hidden="true"><circle cx="8" cy="8" r="7" fill="none" stroke="#fff" stroke-width="1.3"/><path d="M5.6 4.6l1.3 1.6-.7.9c.5 1 1.2 1.7 2.2 2.2l.9-.7 1.6 1.3-.8 1.2c-2.6-.4-4.8-2.6-5.2-5.2z" fill="#fff"/></svg>
    </li>
    <li>info@harbourlinemotion.com
      <svg viewBox="0 0 16 16" aria-hidden="true"><circle cx="8" cy="8" r="7" fill="#fff"/><rect x="4.2" y="5.4" width="7.6" height="5.2" fill="none" stroke="#0b57a8" stroke-width="1"/><path d="M4.2 5.4L8 8.4l3.8-3" fill="none" stroke="#0b57a8" stroke-width="1"/></svg>
    </li>
  </ul>
</section>

<section class="card card-back" aria-label="Business card back">
  <div class="mark-faint"></div>
  <div class="appointment-field field-date"><p class="label">Date</p><div class="rule"></div></div>
  <div class="appointment-field field-time"><p class="label">Time</p><div class="rule"></div></div>
  <div class="appointment-field field-extra"><div class="rule"></div></div>
</section>

</body>
</html>
```